Natural Stone Company Redesign

Looking for a fresh, creative, website design. We service Luxury Residential projects in US and Internationally. We would like to see a design that communicates a passion for creative challenging design that is merged with natural stone projects. Our new company Logo is "Bedrock & Vision"

We like to emphasis from concept to completion, for example, photos of blueprints and/or sketches of a project, then a completion photo of same project.

some websites we like are:
http://www.fernbrockhale.com/
http://lontavimarchitects.com/

We would like to highlight our services of "concept to completion" scenario. Blueprints/sketches to finished products.
Page needed:
Home
About Us
Projects
Contact Us

Target Market(s)

Developers, architects, designers

Industry/Entity Type

It Company

Number of Pages Required

4 page

Font styles to use
Sans Serif

Requirements
Must have
• "Bedrock & Vision"
• New, innovative, look.
• Something to grab the attention, and make them think
Nice to have
• Motion on the homepage
• Roll over the finished project photo, and have the name of the stone pop up

```html
<!DOCTYPE html>
<html lang="en">
<head>
<meta charset="utf-8">
<title>Bedrock &amp; Vision — Home</title>
<link href="https://fonts.googleapis.com/css2?family=Aleo:wght@400;700&family=Roboto:wght@400;500;700&family=Courgette&display=swap" rel="stylesheet">
<style>
:root{
  --red:#e2231a;
  --blue:#2b76c0;
  --ink:#2f2f35;
  --text:#6d6d72;
  --light:#f5f5f5;
  --white:#ffffff;
  --footer:#252a36;
  --footer-line:#353b49;
  --footer-text:#aeb3bf;
  --copy:#1f232d;
}
*{margin:0;padding:0;box-sizing:border-box}
html,body{width:1200px;height:3571px;overflow:hidden}
body{position:relative;font-family:"Roboto",Arial,sans-serif;color:var(--text);background:var(--white)}
.abs{position:absolute}
.heading{font-family:"Aleo",Georgia,serif;font-weight:400;color:var(--ink);font-size:44px;text-align:center;width:100%;left:0}
.rule{position:absolute;width:36px;height:3px;background:var(--red);left:582px}
.btn{position:absolute;display:flex;align-items:center;justify-content:center;background:var(--blue);color:#fff;font-size:12px;font-weight:500;letter-spacing:.5px;border-radius:20px;height:32px;width:120px;text-transform:uppercase}
.para{position:absolute;font-size:13px;line-height:23px;color:var(--text)}

/* hero */
.hero{left:0;top:0;width:1200px;height:648px;background:linear-gradient(180deg,#b9661f 0%,#cf7a26 25%,#8d6a4a 45%,#3f5a36 62%,#4f7a34 80%,#3c6a2a 100%)}
.hero-shade{left:0;top:0;width:1200px;height:648px;background:linear-gradient(180deg,rgba(0,0,0,.25),rgba(0,0,0,0) 30%,rgba(0,0,0,0) 70%,rgba(0,0,0,.25))}
.logo{left:88px;top:36px;font-family:"Aleo",Georgia,serif;font-size:21px;color:#fff;letter-spacing:.5px;text-transform:uppercase}
.nav-line{left:88px;top:88px;width:1024px;height:1px;background:rgba(255,255,255,.3)}
.nav{top:38px;right:90px;display:flex;align-items:center;gap:38px;font-size:13px;color:#fff}
.nav .active{position:relative}
.nav .active::after{content:"";position:absolute;left:-8px;right:-8px;top:49px;height:3px;background:#fff}
.menu{display:flex;flex-direction:column;gap:4px}
.menu i{display:block;width:20px;height:2px;background:#fff}
.hero-title{left:0;width:1200px;top:282px;text-align:center;font-family:"Aleo",Georgia,serif;font-weight:700;font-size:74px;color:#fff}
.hero-sub{left:0;width:1200px;top:366px;text-align:center;font-family:"Courgette",cursive;font-size:28px;color:#fff}
.hero-btn{left:540px;top:412px;height:30px;width:120px;font-size:11px}
.watch{left:90px;top:561px;display:flex;align-items:center;gap:14px;color:#fff}
.watch small{display:block;font-size:11px}
.watch b{font-size:18px;font-weight:500}
.slider{left:553px;top:601px;display:flex;align-items:center;gap:10px}
.slider .dot{width:12px;height:12px;border-radius:50%;border:2px solid #fff}
.slider .dot.on{background:#fff}

/* about */
.about{left:0;top:648px;width:1200px;height:571px;background:var(--light);overflow:hidden}
.ring{right:-70px;top:0;width:142px;height:142px;border:5px solid var(--red);border-radius:50%}
.photo{position:absolute;box-shadow:0 10px 24px rgba(0,0,0,.18)}
.about h2{position:absolute;left:693px;top:142px;font-family:"Aleo",Georgia,serif;font-weight:400;font-size:52px;color:var(--ink)}

/* projects */
.projects{left:0;top:1219px;width:1200px;height:631px;background:var(--white)}
.card{position:absolute;top:176px;width:245px;height:367px;overflow:hidden}
.card .shade{position:absolute;inset:0;background:linear-gradient(180deg,rgba(0,0,0,0) 55%,rgba(0,0,0,.45))}
.diamond{position:absolute;left:106px;top:265px;width:32px;height:32px;background:#fff;transform:rotate(45deg)}
.diamond.on{background:var(--red)}
.num{position:absolute;left:0;width:245px;top:270px;text-align:center;font-size:14px;color:var(--ink)}
.num.on{color:#fff}
.pname{position:absolute;left:0;width:245px;top:312px;text-align:center;font-family:"Aleo",Georgia,serif;font-weight:700;font-size:17px;color:#fff}

/* services */
.services{left:0;top:1850px;width:1200px;height:640px;background:var(--light)}
.svc-title{position:absolute;left:180px;width:392px;top:245px;text-align:center;font-family:"Aleo",Georgia,serif;font-size:25px;color:var(--red)}

/* testimonial */
.testi{left:0;top:2490px;width:1200px;height:520px;background:var(--white)}
.quote{position:absolute;left:0;width:1200px;top:324px;text-align:center;font-size:14px;line-height:24px;color:#55555a}
.who{position:absolute;left:0;width:1200px;top:376px;text-align:center;font-size:13px;color:var(--ink)}
.who span{color:var(--red)}
.tdots{position:absolute;left:581px;top:417px;display:flex;gap:7px}
.tdots i{display:block;width:8px;height:8px;border-radius:50%;background:#c9d6e6}
.tdots i.on{background:#7fa3cc}

/* footer */
.footer{left:0;top:3010px;width:1200px;height:561px;background:var(--footer);color:var(--footer-text)}
.footer .heading{color:#fff}
.contact-item{position:absolute;top:186px;display:flex;gap:14px;align-items:flex-start}
.contact-item b{display:block;color:#fff;font-weight:500;font-size:14px;margin-bottom:4px}
.contact-item span{font-size:12px}
.vline{position:absolute;top:182px;width:1px;height:46px;background:var(--footer-line)}
.contact-btn{position:absolute;left:971px;top:185px;width:139px;height:36px;border-radius:20px;background:#fff;color:var(--ink);font-size:11px;font-weight:500;display:flex;align-items:center;justify-content:center;text-transform:uppercase}
.col{position:absolute;top:304px}
.col h4{color:#fff;font-size:16px;font-weight:500;margin-bottom:14px}
.col li{list-style:none;font-size:12px;line-height:31px;display:flex;align-items:center;gap:8px}
.col li .bullet{width:7px;height:7px;border-radius:50%;background:var(--footer-text)}
.col li.hot{color:var(--red)}
.col li.hot .bullet{background:var(--red)}
.col p{font-size:12px}
.email-field{position:absolute;left:829px;top:371px;width:281px;height:38px;background:#2f3542;display:flex;align-items:center;padding:0 14px;gap:10px;font-size:12px}
.copy{position:absolute;left:0;top:516px;width:1200px;height:45px;background:var(--copy);text-align:center;font-size:12px;line-height:45px}
.totop{position:absolute;left:1146px;top:500px;width:32px;height:32px;border-radius:50%;background:var(--red);display:flex;align-items:center;justify-content:center}
</style>
</head>
<body>

<!-- Hero -->
<section>
  <div class="abs hero" role="img" aria-label="White single-storey house with green lawn and trees under an orange sunset sky"></div>
  <div class="abs hero-shade"></div>
  <div class="abs logo">Bedrock &amp; Vision</div>
  <div class="abs nav-line"></div>
  <nav class="abs nav">
    <span class="active">About Us</span>
    <span>Projects</span>
    <span>Contact Us</span>
    <span class="menu"><i></i><i></i><i></i></span>
  </nav>
  <h1 class="abs hero-title">Inspiration</h1>
  <p class="abs hero-sub">Uisque rutrum aenean imperdiet etiam ultricies</p>
  <div class="btn hero-btn">Get Started</div>
  <div class="abs watch">
    <svg width="40" height="40" viewBox="0 0 40 40"><circle cx="20" cy="20" r="18" fill="none" stroke="#fff" stroke-width="2"/><path d="M16 13 L27 20 L16 27Z" fill="#fff"/></svg>
    <div><small>Watch</small><b>Intro Video</b></div>
  </div>
  <div class="abs slider">
    <svg width="8" height="12" viewBox="0 0 8 12"><path d="M1 1 L6 6 L1 11" fill="none" stroke="#fff" stroke-width="2"/></svg>
    <span class="dot"></span><span class="dot on"></span><span class="dot"></span>
    <svg width="8" height="12" viewBox="0 0 8 12"><rect x="0" y="1" width="2" height="10" fill="#fff"/><rect x="5" y="1" width="2" height="10" fill="#fff"/></svg>
  </div>
</section>

<!-- About -->
<section class="abs about">
  <div class="abs ring"></div>
  <div class="photo" style="left:88px;top:200px;width:193px;height:207px;background:linear-gradient(160deg,#9ab3c9,#8a3a2c 45%,#6f2a22 70%,#7c8a66)" role="img" aria-label="Red wooden house with white trim"></div>
  <div class="photo" style="left:305px;top:90px;width:326px;height:202px;background:linear-gradient(180deg,#2e6fb7 0%,#6fa3d2 40%,#4aa3a8 60%,#b79a72 100%)" role="img" aria-label="Resort pool with loungers and palm trees"></div>
  <div class="photo" style="left:307px;top:316px;width:217px;height:167px;background:linear-gradient(135deg,#1b2fa8,#0e1f8c)" role="img" aria-label="Blueprint sketch of a house"></div>
  <h2>About us</h2>
  <div class="rule" style="left:693px;top:214px"></div>
  <p class="para" style="left:693px;top:242px;width:420px">Quisque rutrum aenean imperdiet etiam ultricies nisi vel augue curabitur ullamcorper ultricies nisi nam eget dui etiam rhoncus maecenas tempus tellus eget condimentum rhoncus sem quam semper libero sit amet adipiscing sem neque sed ipsum. Etiam rhoncus. Maecenas tempus, tellus eget condimentum rhoncus.</p>
  <div class="btn" style="left:688px;top:371px">Read More</div>
</section>

<!-- Projects -->
<section class="abs projects">
  <h2 class="abs heading" style="top:87px">Our Projects</h2>
  <div class="rule" style="top:145px"></div>
  <div class="card" style="left:88px" role="img" aria-label="Grey two-storey house with gable roof and lawn">
    <div style="position:absolute;inset:0;background:linear-gradient(180deg,#4c8fd6,#9ab7c9 40%,#4e7c38 70%,#3e6a2a)"></div>
    <div class="shade"></div><div class="diamond"></div><div class="num">1</div><div class="pname">Project Name Here...</div>
  </div>
  <div class="card" style="left:348px" role="img" aria-label="Blue two-storey house lit at dusk">
    <div style="position:absolute;inset:0;background:linear-gradient(180deg,#5c6a8c,#3b4766 45%,#6d6a62 70%,#4a5a3a)"></div>
    <div class="shade"></div><div class="diamond on"></div><div class="num on">2</div><div class="pname">Project Name Here...</div>
  </div>
  <div class="card" style="left:607px" role="img" aria-label="Traditional pagoda-roof house with garden">
    <div style="position:absolute;inset:0;background:linear-gradient(180deg,#3d78c8,#8fa0a8 35%,#5a4a3a 55%,#4d7a2e)"></div>
    <div class="shade"></div><div class="diamond"></div><div class="num">3</div><div class="pname">Project Name Here...</div>
  </div>
  <div class="card" style="left:864px" role="img" aria-label="Brick house among tall evergreen trees">
    <div style="position:absolute;inset:0;background:linear-gradient(180deg,#3a4a3a,#5a4034 45%,#6a3a2c 65%,#3e4a2e)"></div>
    <div class="shade"></div><div class="diamond"></div><div class="num">4</div><div class="pname">Project Name Here...</div>
  </div>
</section>

<!-- Services -->
<section class="abs services">
  <h2 class="abs heading" style="top:83px">Our Services</h2>
  <div class="rule" style="top:143px"></div>
  <h3 class="svc-title">Concept To Completion</h3>
  <div class="rule" style="left:358px;top:294px"></div>
  <p class="para" style="left:166px;top:305px;width:420px;text-align:center">Quisque rutrum aenean imperdiet etiam ultricies nisi vel augue curabitur ullamcorper ultricies nisi nam eget dui etiam rhoncus maecenas tempus tellus eget condimentum rhoncus sem quam semper libero sit amet adipiscing sem neque sed ipsum. Etiam rhoncus. Maecenas tempus, tellus eget condimentum rhoncus.</p>
  <div class="btn" style="left:318px;top:436px">Read More</div>
  <div class="abs" style="left:634px;top:196px;width:380px;height:356px;background:#fff;box-shadow:0 6px 18px rgba(0,0,0,.12)"></div>
  <div class="abs" style="left:624px;top:186px;width:376px;height:352px;background:linear-gradient(180deg,#e99a2e 0%,#d9822a 35%,#8b7a4e 55%,#3f6a2c 75%,#55802f 100%)" role="img" aria-label="Completed white house with trees at sunset"></div>
</section>

<!-- Testimonial -->
<section class="abs testi">
  <h2 class="abs heading" style="top:80px">What Our Client Says!</h2>
  <div class="rule" style="top:144px"></div>
  <div class="abs" style="left:543px;top:184px;width:114px;height:114px;border-radius:50%;background:radial-gradient(circle at 50% 45%,#c79a7e,#5a3e30 70%,#2e2420)" role="img" aria-label="Client portrait"></div>
  <svg class="abs" style="left:628px;top:188px" width="30" height="30" viewBox="0 0 30 30"><circle cx="15" cy="15" r="14" fill="#2b76c0" stroke="#fff" stroke-width="2"/><path d="M9 18 q0-6 5-8 v2 q-2 1-2 3 h2 v4 h-5z M16 18 q0-6 5-8 v2 q-2 1-2 3 h2 v4 h-5z" fill="#fff"/></svg>
  <p class="quote">" Consectetur adipiscing elit. Etiam eu gravida risus. Aenean lacinia lacus ac nibh bibendum,<br>non mollis urna pellentesque. Maecenas suscipit justo elit."</p>
  <p class="who"><span>clara wynn</span> [Director]</p>
  <div class="tdots"><i></i><i class="on"></i><i></i></div>
</section>

<!-- Footer -->
<footer class="abs footer">
  <h2 class="abs heading" style="top:80px">Contact Us</h2>
  <div class="rule" style="top:144px"></div>

  <div class="contact-item" style="left:88px">
    <svg width="26" height="26" viewBox="0 0 24 24"><path d="M6 3 l3 0 l2 5 l-2 1.5 q1.5 3.5 5 5 l1.5-2 l5 2 l0 3 q-1 2-3 2 q-8-1-12-9 q-1-4 0.5-7.5z" fill="none" stroke="#4a8fd6" stroke-width="1.5"/></svg>
    <div><b>Telephone</b><span>08 (555) 014 2290</span></div>
  </div>
  <div class="vline" style="left:298px"></div>
  <div class="contact-item" style="left:370px">
    <svg width="26" height="26" viewBox="0 0 24 24"><rect x="3" y="6" width="18" height="13" fill="none" stroke="#4a8fd6" stroke-width="1.5"/><path d="M3 6 l9 7 l9-7" fill="none" stroke="#4a8fd6" stroke-width="1.5"/></svg>
    <div><b>Email</b><span>hello@bedrockvision.test</span></div>
  </div>
  <div class="vline" style="left:571px"></div>
  <div class="contact-item" style="left:634px">
    <svg width="26" height="26" viewBox="0 0 24 24"><path d="M12 22 q-7-8-7-12 a7 7 0 0 1 14 0 q0 4-7 12z" fill="none" stroke="#4a8fd6" stroke-width="1.5"/><circle cx="12" cy="10" r="2.5" fill="none" stroke="#4a8fd6" stroke-width="1.5"/></svg>
    <div><b>Address</b><span>some address line goes here, city name</span></div>
  </div>
  <div class="contact-btn">Contact Us</div>

  <div class="col" style="left:90px">
    <h4>Quick Links</h4>
    <ul><li>Home</li><li>About Us</li><li>Projects</li><li>Contact us</li></ul>
  </div>
  <div class="col" style="left:350px">
    <h4>Information</h4>
    <ul><li>Home</li><li>Privacy Policy</li><li>Terms &amp; Condition</li><li>FAQ's</li></ul>
  </div>
  <div class="col" style="left:607px">
    <h4>Follow us</h4>
    <ul>
      <li class="hot"><span class="bullet"></span>Friendwall</li>
      <li><span class="bullet"></span>Chirpline</li>
      <li><span class="bullet"></span>Searchly +</li>
      <li><span class="bullet"></span>Workweb</li>
    </ul>
  </div>
  <div class="col" style="left:829px">
    <h4>Subscribe To Our Newsletter</h4>
    <p>Subscribe to our newsletter to get the latest news.</p>
  </div>
  <div class="email-field">
    <svg width="16" height="12" viewBox="0 0 16 12"><rect x="1" y="1" width="14" height="10" fill="none" stroke="#aeb3bf"/><path d="M1 1 l7 5 l7-5" fill="none" stroke="#aeb3bf"/></svg>
    <span style="flex:1">Email address</span>
    <svg width="16" height="16" viewBox="0 0 16 16"><path d="M1 8 L15 1 L11 15 L8 9Z" fill="#fff"/></svg>
  </div>

  <div class="copy">© 2017, All Rights Reserved.</div>
  <div class="totop"><svg width="12" height="8" viewBox="0 0 12 8"><path d="M1 7 L6 2 L11 7" fill="none" stroke="#fff" stroke-width="2"/></svg></div>
</footer>

</body>
</html>
```